Australian Civil Construction, Quarry & Mining Services needs a business card

We need a business card designed for our Civil Construction, Quarry & Mining Services based in the country in Australia.
Our Company Brackley Earthworks provide innovate solutions for infrastructure, agricultural and mining (aggregate, sand, roadbase) industry.
We would like our business cards to be double sided
Front of card: black background or something that resembles our business colours. (it doesn't have to be black we are open to options)
- Company name - Brackley Earthworks
- Either our logo or some sort of icon/picture that resembles our business
- Website - https://brackleyearthworks.com.au/
- We will have a number of different names, positions descriptions, phone numbers and emails on separate cards for each of our managers/directors

```html
<!DOCTYPE html>
<html lang="en">
<head>
<meta charset="utf-8">
<title>Brackley Earthworks – Business Card</title>
<link rel="stylesheet" href="https://fonts.googleapis.com/css2?family=Montserrat:wght@400;500;700;800&display=swap">
<style>
  :root {
    --page-bg: #2b2b2d;
    --card-white: #ffffff;
    --card-white-edge: #ececec;
    --ink: #111111;
    --ink-soft: #333333;
    --accent: #f07a12;
    --sky-top: #3a4048;
    --sky-mid: #6b5a4a;
    --sky-glow: #b98a4e;
    --ground: #2a2420;
    --overlay: rgba(20, 18, 16, 0.45);
    --text-light: #f4f1ec;
  }
  * { box-sizing: border-box; margin: 0; padding: 0; }
  html, body {
    width: 1200px; height: 900px; overflow: hidden;
    background: var(--page-bg);
    font-family: "Montserrat", Arial, sans-serif;
  }
  .stage {
    width: 1200px; height: 900px;
    display: flex; flex-direction: column;
    align-items: center; justify-content: center; gap: 40px;
  }
  .card {
    width: 680px; height: 389px;
    border-radius: 22px;
    position: relative; overflow: hidden;
    box-shadow: 0 12px 30px rgba(0,0,0,0.45);
  }

  /* Front: personal details */
  .card-front {
    background: linear-gradient(135deg, var(--card-white) 0%, var(--card-white) 55%, var(--card-white-edge) 100%);
  }
  .person {
    position: absolute; left: 40px; top: 128px;
    width: 292px;
    text-align: right;
  }
  .person-name {
    font-size: 32px; font-weight: 800; color: var(--ink);
    letter-spacing: -0.5px; line-height: 1.05;
    white-space: nowrap; text-align: left;
  }
  .person-name .surname { color: var(--accent); }
  .person-role {
    margin-top: 8px;
    font-size: 15px; font-weight: 500; color: var(--ink-soft);
  }
  .divider {
    position: absolute; left: 350px; top: 112px;
    width: 2px; height: 168px; background: var(--accent);
  }
  .contact {
    position: absolute; left: 372px; top: 118px;
    width: 290px;
    font-size: 15px; font-weight: 500; color: var(--ink);
    line-height: 1.5;
  }
  .contact-address { margin-bottom: 8px; }
  .contact-line { display: flex; align-items: center; gap: 9px; white-space: nowrap; }
  .contact-line svg { width: 13px; height: 13px; flex: none; }

  /* Back: company side */
  .card-back { background: var(--ground); }
  .site-photo {
    position: absolute; inset: 0;
    background:
      linear-gradient(180deg, transparent 60%, var(--ground) 100%),
      radial-gradient(ellipse at 70% 75%, var(--sky-glow) 0%, transparent 55%),
      linear-gradient(180deg, var(--sky-top) 0%, var(--sky-mid) 60%, var(--ground) 100%);
  }
  .site-photo::after {
    content: ""; position: absolute; inset: 0; background: var(--overlay);
  }
  .brand-badge {
    position: absolute; right: 60px; top: 34px;
    width: 170px; height: 170px; border-radius: 50%;
    background: var(--card-white);
    box-shadow: 0 6px 14px rgba(0,0,0,0.4);
    display: flex; align-items: center; justify-content: center;
    text-align: center;
    font-size: 18px; font-weight: 800; color: var(--accent);
    line-height: 1.15; text-transform: uppercase;
  }
  .brand-text {
    position: absolute; right: 60px; top: 232px; text-align: right;
    color: var(--text-light);
  }
  .brand-name {
    font-size: 29px; font-weight: 700; letter-spacing: 2.5px;
    text-transform: uppercase; white-space: nowrap;
  }
  .brand-tagline {
    margin-top: 10px;
    font-size: 14px; font-weight: 500; letter-spacing: 1.2px;
    text-transform: uppercase; white-space: nowrap;
  }
</style>
</head>
<body>
<main class="stage">

  <section class="card card-front" aria-label="Business card front">
    <div class="person">
      <h1 class="person-name">Maren <span class="surname">Ostrowski</span></h1>
      <p class="person-role">Payroll Manager</p>
    </div>
    <div class="divider"></div>
    <div class="contact">
      <p class="contact-address">42 Quarry Ridge Rd.<br>Unit 7 Dubbo NSW 2830</p>
      <p class="contact-line">
        <svg viewBox="0 0 24 24" aria-hidden="true"><path fill="#f07a12" d="M6.6 10.8a15.1 15.1 0 0 0 6.6 6.6l2.2-2.2a1 1 0 0 1 1-.25 11.4 11.4 0 0 0 3.6.57 1 1 0 0 1 1 1V20a1 1 0 0 1-1 1A17 17 0 0 1 3 4a1 1 0 0 1 1-1h3.5a1 1 0 0 1 1 1c0 1.25.2 2.45.57 3.57a1 1 0 0 1-.25 1z"/></svg>
        (02) 5550 1842
      </p>
      <p class="contact-line">
        <svg viewBox="0 0 24 24" aria-hidden="true"><rect x="2.5" y="5" width="19" height="14" rx="1.5" fill="none" stroke="#f07a12" stroke-width="2"/><path d="M3 6l9 7 9-7" fill="none" stroke="#f07a12" stroke-width="2"/></svg>
        info@brackleyearthworks.com.au
      </p>
      <p class="contact-line">
        <svg viewBox="0 0 24 24" aria-hidden="true"><circle cx="12" cy="12" r="9.5" fill="none" stroke="#f07a12" stroke-width="2"/><path d="M2.5 12h19M12 2.5c3 3 3 16 0 19M12 2.5c-3 3-3 16 0 19" fill="none" stroke="#f07a12" stroke-width="1.6"/></svg>
        www.brackleyearthworks.com.au
      </p>
    </div>
  </section>

  <section class="card card-back" aria-label="Business card back">
    <div class="site-photo" role="img" aria-label="Photo of an excavator on a work site under a cloudy sunset sky"></div>
    <div class="brand-badge">Brackley<br>Earthworks</div>
    <div class="brand-text">
      <p class="brand-name">Brackley Earthworks</p>
      <p class="brand-tagline">Civil Construction, Quarry &amp; Mining Services</p>
    </div>
  </section>

</main>
</body>
</html>
```